BrightLoop Vents Services need a Business Card!

Need a business card designed for a new start company called BrightLoop! I have attached a Zip file (Please let me know if you cannot open this file) with all logos and also a sheets that includes fonts and colors. Last, you will see the design of our vans which will help design the cards too!
The card is needing to be double sided. A place for email, name, headshot, cell #, Office #, Service Manager (Head shot optional)

Target Market(s)

People who need their HVAC filters changed. Residential and Commercial

Industry/Entity Type

Hvac Filter Changing Service

Contact Information for Business Card

Website: BrightLoopVents.us Office phone: 517.268.3390 The card is needing to be double sided. A place for email, name, headshot, cell #, Office #, Service Manager (Head shot optional)

Requirements
Must have
• Color code and fonts form attached sheets and files

```html
<!DOCTYPE html>
<html lang="en">
<head>
<meta charset="utf-8">
<title>BrightLoop Vents Services – Business Card</title>
<link rel="stylesheet" href="https://fonts.googleapis.com/css2?family=Montserrat:wght@500;600;700&family=Roboto:wght@400&display=swap">
<style>
  :root {
    --stage-top: #475560;
    --stage-bottom: #0f1114;
    --card-deep: #03458e;
    --card-mid: #1b5fa9;
    --card-light: #3a7dc4;
    --accent-cyan: #00a8e6;
    --white: #ffffff;
    --soft-white: #d6e6f7;
    --ink: #111111;
    --label: #f2f2f2;
  }
  * { margin: 0; padding: 0; box-sizing: border-box; }
  html, body { width: 1005px; height: 1200px; overflow: hidden; }
  body {
    position: relative;
    background: linear-gradient(180deg, var(--stage-top) 0%, #2a3038 50%, var(--stage-bottom) 100%);
    font-family: "Montserrat", sans-serif;
  }
  .card {
    position: absolute;
    left: 133px;
    width: 739px;
    height: 421px;
    border-radius: 31px;
    overflow: hidden;
    background: linear-gradient(25deg, var(--card-deep) 0%, var(--card-deep) 30%, var(--card-mid) 55%, var(--card-light) 80%);
    box-shadow: 0 18px 30px rgba(0,0,0,0.55);
  }
  .card--front { top: 86px; }
  .card--back { top: 623px; }
  .side-label {
    position: absolute;
    left: 0; width: 1005px;
    text-align: center;
    font-family: "Roboto", sans-serif;
    font-size: 23px;
    color: var(--label);
  }
  .side-label--front { top: 551px; }
  .side-label--back { top: 1086px; }

  .brand-name {
    font-weight: 600;
    color: var(--white);
    letter-spacing: 0.5px;
    display: flex;
    align-items: center;
  }
  .brand-dot {
    display: inline-block;
    border-radius: 50%;
    background: var(--accent-cyan);
  }
  .front-brand {
    position: absolute;
    inset: 0;
    justify-content: center;
    font-size: 44px;
    gap: 14px;
  }
  .front-brand .brand-dot { width: 30px; height: 30px; }

  .back-brand {
    position: absolute;
    left: 33px; top: 34px;
    font-size: 64px;
    gap: 16px;
    line-height: 1;
  }
  .back-brand .brand-dot { width: 40px; height: 40px; }

  .tagline {
    position: absolute;
    right: 46px; top: 120px;
    font-size: 30px;
    font-weight: 700;
    color: var(--white);
  }
  .swoosh { position: absolute; left: 0; top: 0; }

  .cardholder {
    position: absolute;
    left: 33px; top: 196px;
    color: var(--white);
  }
  .cardholder-name {
    font-size: 21px;
    font-weight: 600;
    line-height: 1.2;
  }
  .cardholder-title {
    font-size: 14px;
    font-weight: 500;
    color: var(--soft-white);
    margin-top: 4px;
  }
  .cardholder-cell {
    font-size: 15px;
    font-weight: 500;
    margin-top: 14px;
  }

  .contact-list {
    position: absolute;
    right: 40px; top: 0;
    list-style: none;
  }
  .contact-item {
    position: absolute;
    right: 0;
    display: flex;
    align-items: center;
    gap: 16px;
    font-size: 16px;
    font-weight: 500;
    color: var(--ink);
    text-align: right;
    line-height: 1.2;
    white-space: nowrap;
  }
  .contact-item--web { top: 209px; }
  .contact-item--mail { top: 253px; }
  .contact-item--place { top: 301px; }
  .contact-item--phone { top: 356px; }
  .contact-icon {
    width: 30px; height: 30px;
    border-radius: 50%;
    background: var(--accent-cyan);
    display: flex; align-items: center; justify-content: center;
    flex-shrink: 0;
  }
</style>
</head>
<body>

<section class="card card--front">
  <div class="brand-name front-brand"><span class="brand-dot"></span>BrightLoop</div>
</section>
<p class="side-label side-label--front">(front)</p>

<section class="card card--back">
  <div class="brand-name back-brand"><span class="brand-dot"></span>BrightLoop</div>
  <p class="tagline">Vents Services</p>

  <svg class="swoosh" width="739" height="421" viewBox="0 0 739 421" aria-hidden="true">
    <defs>
      <linearGradient id="bandFade" x1="0" y1="1" x2="1" y2="0">
        <stop offset="0" stop-color="#00aeea"/>
        <stop offset="0.55" stop-color="#0091d4"/>
        <stop offset="1" stop-color="#0a4e9c"/>
      </linearGradient>
    </defs>
    <path d="M739,167 C420,183 168,292 136,421 L184,421 C232,282 452,187 739,167 Z" fill="url(#bandFade)"/>
    <path d="M739,167 C452,187 232,282 184,421 L739,421 Z" fill="#ffffff"/>
  </svg>

  <div class="cardholder">
    <p class="cardholder-name">Jordan Avery</p>
    <p class="cardholder-title">Service Manager</p>
    <p class="cardholder-cell">Cell 517.268.4471</p>
  </div>

  <ul class="contact-list">
    <li class="contact-item contact-item--web">
      <span>brightloopvents.us</span>
      <span class="contact-icon">
        <svg width="18" height="18" viewBox="0 0 24 24" fill="none" stroke="#fff" stroke-width="2.2" stroke-linecap="round"><path d="M10 14a4 4 0 0 0 5.6 0l3-3a4 4 0 0 0-5.6-5.6l-1 1"/><path d="M14 10a4 4 0 0 0-5.6 0l-3 3a4 4 0 0 0 5.6 5.6l1-1"/></svg>
      </span>
    </li>
    <li class="contact-item contact-item--mail">
      <span>contact@brightloopvents.us</span>
      <span class="contact-icon">
        <svg width="18" height="18" viewBox="0 0 24 24" fill="none" stroke="#fff" stroke-width="2"><rect x="3" y="6" width="18" height="12" rx="1"/><path d="M3 6l9 7 9-7M3 18l7-6M21 18l-7-6"/></svg>
      </span>
    </li>
    <li class="contact-item contact-item--place">
      <span>General address only<br>for personal security</span>
      <span class="contact-icon">
        <svg width="16" height="18" viewBox="0 0 24 24"><path d="M12 2a7 7 0 0 0-7 7c0 5 7 13 7 13s7-8 7-13a7 7 0 0 0-7-7z" fill="#fff"/><circle cx="12" cy="9" r="2.8" fill="#00a8e6"/></svg>
      </span>
    </li>
    <li class="contact-item contact-item--phone">
      <span>517.268.3390</span>
      <span class="contact-icon">
        <svg width="17" height="17" viewBox="0 0 24 24"><path d="M6.6 10.8a15 15 0 0 0 6.6 6.6l2.2-2.2a1 1 0 0 1 1-.25 11.4 11.4 0 0 0 3.6.57 1 1 0 0 1 1 1V20a1 1 0 0 1-1 1A17 17 0 0 1 3 4a1 1 0 0 1 1-1h3.5a1 1 0 0 1 1 1 11.4 11.4 0 0 0 .57 3.6 1 1 0 0 1-.25 1z" fill="#fff"/></svg>
      </span>
    </li>
  </ul>
</section>
<p class="side-label side-label--back">(back)</p>

</body>
</html>
```